Design of labels for exciting new natural skincare products...natural deodorant

I need some labels designed for a range of natural skincare, initially a natural deodorant paste. i will be offering a range of fragrances so i want a basic idea that i can drop different colours / ingredients into easily.

Fragrances are:
1. Jasmine, Orange and Bergamot
2. Lavender & Bergamot
3. Peppermint & Tea tree
4. Unscented
5. Lime, Lemongrass & Ginger

I am a new startup and will be selling online and through a couple of specialty online stores. The final design should encompass our ethos which is clean and green, not fussy nor clinical but friendly and easily accessible. I like fresh, contemporary modern look referencing vintage aesthetics.

The idea is that these products are better for your body AND the environment, and we pledge to use no plastic to package or distribute our products. i like the use of contemporary pastels such as soft pinks, tans and green/blue/aquas, though am open to new ideas too. the logo (attached) appears in red but that should not necessarily be used. i also like black and white with touches of colour.

Target Market(s)

Eco aware, health concious consumers with a reasonable skincare budget.

Industry/Entity Type

Skin Care Product

Font styles to use
Serif
Sans Serif
Decorative

Colors
2eb6a2
b768aa
eea4c8
fabb94
85cae6
cfeae6
eaf2ce
000000
eaeaea

Requirements
Must have
• Labels are for a small glass jar - the dimensions are 2cm high only and wrapping around the jar - at least 10cm wide. i'm also going to be providing a smaller size so this needs to be able to scale down to 1.5cm high and 8cm wide.
• the logo (supplied)
• title: Natural Deodorant
• Subtitle: Orange, Jasmine & Bergamot
• 45g
• Ingredients: tapioca starch*, bicarbonate of soda, Coconut oil*, shea butter*, mango butter*, diatomaceous earth*, sweet almond oil*, vitamin e*, tea tree oil*, Sweet orange essential oil*, Jasmine essential oil*, Bergamot essential oil*.
• *Certified organic ingredient
• (DESIGNERS - PLEASE NOTE NOT ALL THE INGREDIENTS ARE ORGANIC, PLEASE LIST THEM WITH A STAR * IF I HAVE SUPPLIED IT, THEN *Certified organic ingredient BELOW IN SLIGHTLY SMALLER TEXT - THIS SERVES AS THE KEY FOR THE INGREDIENTS LIST)
• pebblewick.nz
• Massage a pea-sized amount onto clean, dry armpits for an odour-free day.
• If irritation develops discontinue use and contact Fern Hollow. (please italicise the company name)
Nice to have
• open to ideas - i am attaching some examples of designs i like, you'll notice i swing between plain black and white aesthetics and a more decorative look. In general i like the old "medicine bottle" look, with hand sketched illustrations. But i'm open to ideas!

```html
<!DOCTYPE html>
<html lang="en">
<head>
<meta charset="utf-8">
<title>Fern Hollow – Natural Deodorant Labels</title>
<link rel="stylesheet" href="https://fonts.googleapis.com/css2?family=Montserrat:wght@400;500;600;700&family=Arimo:wght@400&display=swap">
<style>
  :root {
    --teal: #2eb6a2;
    --mint: #cfeae6;
    --ink: #222222;
    --ink-soft: #2b2b2b;
    --grey: #7a7a7a;
    --frame-grey: #555555;
    --paper: #ffffff;
  }
  * { box-sizing: border-box; margin: 0; padding: 0; }
  html, body {
    width: 1200px; height: 738px; overflow: hidden;
    background: var(--paper);
    font-family: "Montserrat", sans-serif;
  }
  .canvas { position: relative; width: 1200px; height: 738px; }

  .variant-caption {
    position: absolute; left: 0; width: 1200px; text-align: center;
    font-family: "Arimo", Arial, sans-serif; font-size: 15px; color: #222;
    letter-spacing: -0.1px;
  }

  .label {
    position: absolute; left: 156px; width: 888px; height: 178px;
    background: var(--paper); border: 1px solid var(--frame-grey);
  }
  .label__frame {
    position: absolute; left: 8px; top: 8px; width: 871px; height: 162px;
    border: 2px solid var(--teal);
  }
  .label__divider {
    position: absolute; top: 18px; width: 2px; height: 142px; background: #333;
  }
  .label__divider--left { left: 298px; }
  .label__divider--right { left: 801px; }

  .label__brand {
    position: absolute; left: 34px; width: 240px; top: 42px;
    text-align: center; font-weight: 700; font-size: 34px; line-height: 40px;
    color: var(--teal); letter-spacing: -0.5px;
  }
  .label__title {
    position: absolute; left: 14px; width: 280px; top: 119px;
    text-align: center; font-weight: 500; font-size: 18px; line-height: 22px;
    color: var(--ink); letter-spacing: 0.6px; word-spacing: 3px;
  }
  .label__subtitle {
    position: absolute; left: 14px; width: 280px; top: 145px;
    text-align: center; font-weight: 400; font-size: 15px; line-height: 18px;
    color: var(--grey);
  }

  .ingredients { position: absolute; left: 317px; top: 18px; width: 468px; color: var(--ink-soft); }
  .ingredients__heading { font-weight: 600; font-size: 18.5px; line-height: 24px; }
  .ingredients__list {
    margin-top: 2px; font-weight: 600; font-size: 14.6px; line-height: 21.6px;
    text-align: justify; text-align-last: left;
  }
  .ingredients__key {
    position: absolute; left: 317px; top: 139px;
    font-weight: 600; font-size: 15px; line-height: 18px; color: var(--ink-soft);
  }

  .label__mark { position: absolute; left: 821px; top: 71px; width: 38px; height: 38px; }
  .label__weight {
    position: absolute; left: 800px; width: 80px; top: 137px; text-align: center;
    font-weight: 700; font-size: 20px; line-height: 24px; color: var(--ink-soft);
  }

  /* colour background variant */
  .label--colour { background: var(--teal); border-color: var(--teal); }
  .label--colour .label__frame { border: 1.5px solid var(--mint); }
  .label--colour .label__divider { background: var(--mint); width: 1.5px; }
  .label--colour .label__brand { color: var(--mint); }
  .label--colour .label__subtitle { color: var(--mint); }
  .label--colour .label__title { color: #1c2725; letter-spacing: 0.3px; word-spacing: 0; }
</style>
</head>
<body>
<main class="canvas">

  <p class="variant-caption" style="top:117px;">FERN HOLLOW with WHITE BACKGROUND</p>
  <section class="label label--white" style="top:138px;">
    <div class="label__frame"></div>
    <p class="label__brand">Fern Hollow</p>
    <h2 class="label__title">NATURAL DEODORANT</h2>
    <p class="label__subtitle">Orange, Jasmine &amp; Bergamot</p>
    <span class="label__divider label__divider--left"></span>
    <div class="ingredients">
      <h3 class="ingredients__heading">Ingredients:</h3>
      <p class="ingredients__list">Coconut oil*, tapioca starch*, bicarbonate of soda, shea butter*, mango butter*, diatomaceous earth*, sweet almond oil*, vitamin e*, tea tree oil*, Sweet orange essential oil*, Jasmine essential oil*, Bergamot essential oil*</p>
    </div>
    <p class="ingredients__key">*Certified organic ingredient</p>
    <span class="label__divider label__divider--right"></span>
    <svg class="label__mark" viewBox="0 0 38 38" role="img" aria-label="Packaging certification badge"><circle cx="19" cy="19" r="18" fill="#222"/></svg>
    <p class="label__weight">50g</p>
  </section>

  <p class="variant-caption" style="top:417px;">FERN HOLLOW with COLOR BACKGROUND</p>
  <section class="label label--colour" style="top:440px;">
    <div class="label__frame"></div>
    <p class="label__brand">Fern Hollow</p>
    <h2 class="label__title">NATURAL DEODORANT</h2>
    <p class="label__subtitle">Orange, Jasmine &amp; Bergamot</p>
    <span class="label__divider label__divider--left"></span>
    <div class="ingredients">
      <h3 class="ingredients__heading">Ingredients:</h3>
      <p class="ingredients__list">Coconut oil*, tapioca starch*, bicarbonate of soda, shea butter*, mango butter*, diatomaceous earth*, sweet almond oil*, vitamin e*, tea tree oil*, Sweet orange essential oil*, Jasmine essential oil*, Bergamot essential oil*</p>
    </div>
    <p class="ingredients__key">*Certified organic ingredient</p>
    <span class="label__divider label__divider--right"></span>
    <svg class="label__mark" viewBox="0 0 38 38" role="img" aria-label="Packaging certification badge"><circle cx="19" cy="19" r="18" fill="#222"/></svg>
    <p class="label__weight">50g</p>
  </section>

</main>
</body>
</html>
```